Business Card Update, need to bring life to the card, two sided color

We need a new business card design, are moving and changing addresses and need a new look, we have the logos already attached but need a new style moving forward. Can incorporate the color of the logo (The Green) as well, maybe a solid back? We deal with safety products revolving around static electricity and safety lighting. Would like to keep same font in second logo as well.

Target Market(s)

Electrical Safety, Lighting

Contact Information for Business Card

Lars Whitcombe
Vice Vice President
Office: 555-284-7316
Cell: 555-862-0457
lars@tkwhitcombe.com
www.tkwhitcombe.com
4700 West Cedar Boulevard
Suite #320
Roswell, GA 30412

Font styles to use
Serif
Sans Serif

Requirements
Must have
• Since 1918
Nice to have
• Could use the 100 Year Logo for back of card, would like the back of card to be the same green as logo.
Should not have
• No black cards please.

```html
<!DOCTYPE html>
<html lang="en">
<head>
<meta charset="utf-8">
<title>T.K. Whitcombe Business Card</title>
<link href="https://fonts.googleapis.com/css2?family=Arimo:wght@700&family=Source+Sans+3:wght@400&display=swap" rel="stylesheet">
<style>
  :root {
    --brand-green: #00985b;
    --backdrop: #e5eae8;
    --frame: #1c1c1c;
    --ink: #111111;
    --paper: #ffffff;
    --swoosh-grey: #b9b9bf;
    --rule: #9a9a9a;
  }
  html, body { margin: 0; padding: 0; overflow: hidden; }
  .canvas {
    position: relative;
    width: 1200px; height: 798px;
    background: var(--backdrop);
    box-sizing: border-box;
    border: 3px solid var(--frame);
    overflow: hidden;
  }
  .card { position: absolute; overflow: hidden; }
  .card-front {
    left: 30px; top: 17px; width: 652px; height: 373px;
    background: var(--paper);
    border-radius: 33px 33px 22px 22px;
  }
  .card-back {
    left: 489px; top: 395px; width: 673px; height: 384px;
    background: var(--brand-green);
    border-radius: 33px;
  }
  .brand-mark { position: absolute; border-radius: 50%; }
  .front-mark {
    left: 38px; top: 139px; width: 82px; height: 82px;
    background: var(--brand-green);
  }
  .back-mark {
    left: 38px; top: 111px; width: 138px; height: 138px;
    background: var(--ink);
  }
  .brand-name, .brand-sub, .brand-since {
    position: absolute; margin: 0; white-space: nowrap;
    font-family: "Arimo", Arial, sans-serif; font-weight: 700;
  }
  .front-name  { left: 134px; top: 155px; font-size: 25px; color: var(--brand-green); }
  .front-sub   { left: 134px; top: 186px; font-size: 13px; color: var(--brand-green); }
  .front-since { left: 134px; top: 204px; font-size: 13px; color: var(--brand-green); }
  .back-name   { left: 200px; top: 140px; font-size: 50px; color: var(--ink); }
  .back-sub    { left: 200px; top: 198px; font-size: 23px; color: var(--ink); }
  .back-since  { left: 200px; top: 230px; font-size: 18px; color: var(--ink); }
  .divider {
    position: absolute; left: 384px; top: 100px;
    width: 1px; height: 150px; background: var(--rule);
  }
  .contact {
    position: absolute; left: 398px; top: 96px;
    margin: 0; padding: 0; list-style: none;
    font-family: "Source Sans 3", "Myriad Pro", sans-serif;
    font-size: 16px; color: var(--ink); line-height: 20px;
  }
  .contact li { display: flex; align-items: center; }
  .contact .address { display: block; margin-bottom: 9px; }
  .contact .line { margin-bottom: 4px; }
  .contact svg { width: 14px; height: 14px; margin-right: 6px; flex: none; }
  .wave { position: absolute; left: 0; top: 0; }
  .person {
    position: absolute; left: 68px; top: 295px;
    font-family: "Arimo", Arial, sans-serif; font-weight: 700;
  }
  .person-name { margin: 0; font-size: 25px; color: var(--paper); line-height: 30px; }
  .person-role { margin: 0; font-size: 19px; color: var(--ink); line-height: 26px; }
  .back-web {
    position: absolute; left: 0; right: 0; bottom: 12px; margin: 0;
    text-align: center;
    font-family: "Source Sans 3", "Myriad Pro", sans-serif;
    font-size: 21px; letter-spacing: 4.5px; color: var(--ink);
  }
</style>
</head>
<body>
<div class="canvas">

  <section class="card card-front">
    <svg class="wave" width="652" height="373" viewBox="0 0 652 373" aria-hidden="true">
      <path d="M0 296 C130 270 270 282 380 310 C470 333 570 340 652 334 L652 373 L0 373 Z" fill="var(--brand-green)"/>
      <path d="M0 290 C90 272 200 270 300 290 C200 276 90 278 0 296 Z" fill="var(--brand-green)"/>
      <path d="M170 271 C270 268 360 290 460 318 C540 338 610 340 652 332 L652 335 C610 344 540 342 460 322 C360 294 270 272 170 271 Z" fill="var(--swoosh-grey)"/>
      <path d="M350 305 C430 322 530 330 652 306 L652 318 C560 338 450 330 350 305 Z" fill="var(--ink)"/>
    </svg>

    <span class="brand-mark front-mark"></span>
    <p class="brand-name front-name">T.K. Whitcombe</p>
    <p class="brand-sub front-sub">Manufacturing Company, Inc.</p>
    <p class="brand-since front-since">Since 1918</p>

    <span class="divider"></span>

    <ul class="contact">
      <li class="address">4700 West Cedar Boulevard<br>Suite #320, Roswell, GA 30412</li>
      <li class="line">
        <svg viewBox="0 0 14 14"><circle cx="7" cy="7" r="6" fill="none" stroke="var(--brand-green)" stroke-width="1.4"/><path d="M4.6 4 L6 4.2 L6.2 5.6 L5.5 6.2 C6 7.3 6.7 8 7.8 8.5 L8.4 7.8 L9.8 8 L10 9.4 C7 10 4 7 4.6 4 Z" fill="var(--brand-green)"/></svg>
        Office: 555-284-7316
      </li>
      <li class="line">
        <svg viewBox="0 0 14 14"><circle cx="7" cy="7" r="6" fill="none" stroke="var(--brand-green)" stroke-width="1.4"/><rect x="5" y="3.5" width="4" height="7" rx="0.8" fill="var(--brand-green)"/><rect x="5.8" y="4.5" width="2.4" height="4" fill="var(--paper)"/></svg>
        Cell: 555-862-0457
      </li>
      <li class="line">
        <svg viewBox="0 0 14 14" fill="none" stroke="var(--brand-green)" stroke-width="1.1"><circle cx="7" cy="7" r="6"/><ellipse cx="7" cy="7" rx="2.6" ry="6"/><path d="M1 7 H13 M2 4 H12 M2 10 H12"/></svg>
        www.tkwhitcombe.com
      </li>
      <li class="line">
        <svg viewBox="0 0 14 14"><circle cx="7" cy="7" r="6" fill="none" stroke="var(--brand-green)" stroke-width="1.4"/><rect x="4" y="5" width="6" height="4.2" fill="var(--brand-green)"/><path d="M4 5 L7 7.3 L10 5" fill="none" stroke="var(--paper)" stroke-width="0.8"/></svg>
        lars@tkwhitcombe.com
      </li>
    </ul>

    <div class="person">
      <p class="person-name">Lars Whitcombe</p>
      <p class="person-role">Vice President</p>
    </div>
  </section>

  <section class="card card-back">
    <span class="brand-mark back-mark"></span>
    <p class="brand-name back-name">T.K. Whitcombe</p>
    <p class="brand-sub back-sub">Manufacturing Company, Inc.</p>
    <p class="brand-since back-since">Since 1918</p>
    <p class="back-web">www.tkwhitcombe.com</p>
  </section>

</div>
</body>
</html>
```